Used Car Dealer seeks an Amazing Business Card Design

We are looking for a business card design that incorporates our logo and grabs the attention of anyone we give the business card to.

Looking to use the same colors as the logo. Our Logo choice is the black background with Red and Silver/Grey Lettering.

We also would like to see some embossed designs.

Target Market(s)

Used Car Buyers, Automotive, Auto

Industry/Entity Type

Automotive

Contact Information for Business Card

BVEL7K
Gordon Whitlock
482 Tarrow Lane
Suite 207
Brenford, GA 30412
Office (770) 555-0142
Cell (770) 555-0187
bvel7kga@quellmail.com
www.bvel7kga.com

Colors
ffffff
ee3036

Requirements
Must have
• Must include our logo (Black Background with Red and Silver/Grey Lettering)
Nice to have
• Embossed Design. Can be Single or Double Sided.

```html
<!DOCTYPE html>
<html lang="en">
<head>
<meta charset="utf-8">
<title>BVEL7K Business Card</title>
<link rel="stylesheet" href="https://fonts.googleapis.com/css2?family=Noto+Sans:wght@400;700&display=swap">
<style>
  :root {
    --page-bg: #e4e4e6;
    --card-dark: #2c2d3e;
    --card-light: #f7f7f7;
    --brand-red: #ee3036;
    --brand-red-deep: #b8222a;
    --brand-silver: #c8cbd2;
    --icon-gold: #f6b93f;
    --ink: #1e1e24;
    --ink-soft: #3a3a44;
  }
  * { box-sizing: border-box; margin: 0; padding: 0; }
  html, body { width: 1200px; height: 800px; overflow: hidden; }
  body {
    background: var(--page-bg);
    font-family: "Noto Sans", Verdana, sans-serif;
    position: relative;
  }
  .card {
    position: absolute;
    left: 75px;
    top: 100px;
    width: 1050px;
    height: 600px;
    background: var(--card-light);
    border-radius: 6px;
    overflow: hidden;
    box-shadow: 0 10px 30px rgba(0,0,0,0.18);
  }
  .card-shapes { position: absolute; inset: 0; }
  .brand-name {
    position: absolute;
    left: 90px;
    top: 200px;
    font-size: 92px;
    font-weight: 700;
    color: var(--brand-silver);
    letter-spacing: 2px;
  }
  .holder-name {
    position: absolute;
    left: 630px;
    top: 80px;
    font-size: 48px;
    font-weight: 700;
    color: #ffffff;
    white-space: nowrap;
  }
  .holder-title {
    position: absolute;
    left: 650px;
    top: 170px;
    font-size: 30px;
    letter-spacing: 12px;
    color: var(--ink-soft);
  }
  .contact-row {
    position: absolute;
    display: flex;
    align-items: flex-start;
    gap: 22px;
    font-size: 30px;
    line-height: 37px;
    color: var(--ink);
    white-space: nowrap;
  }
  .contact-icon {
    flex: none;
    width: 40px;
    height: 40px;
    margin-top: -2px;
  }
</style>
</head>
<body>
  <div class="card">
    <svg class="card-shapes" width="1050" height="600" viewBox="0 0 1050 600">
      <polygon points="0,0 690,0 300,600 0,600" fill="var(--card-dark)"/>
      <polygon points="560,55 620,55 620,170 560,150" fill="var(--brand-red-deep)"/>
      <rect x="600" y="70" width="450" height="100" fill="var(--brand-red)"/>
    </svg>

    <div class="brand-name">BVEL7K</div>

    <div class="holder-name">Gordon Whitlock</div>
    <div class="holder-title">Manager</div>

    <div class="contact-row" style="left:555px; top:250px;">
      <svg class="contact-icon" viewBox="0 0 40 40"><circle cx="20" cy="20" r="20" fill="var(--icon-gold)"/><path d="M13 11c2-1 3 0 4 2l1 3c0 1-1 2-2 2 1 3 3 5 6 6 0-1 1-2 2-2l3 1c2 1 3 2 2 4-1 2-3 3-5 2-6-2-10-6-12-12-1-2 0-5 1-6z" fill="#fff"/></svg>
      <span>(770) 555-0142</span>
    </div>

    <div class="contact-row" style="left:522px; top:302px;">
      <svg class="contact-icon" viewBox="0 0 40 40"><circle cx="20" cy="20" r="20" fill="var(--icon-gold)"/><rect x="14" y="9" width="12" height="22" rx="2" fill="#fff"/><rect x="16" y="12" width="8" height="10" fill="var(--icon-gold)"/></svg>
      <span>(770) 555-0187</span>
    </div>

    <div class="contact-row" style="left:488px; top:356px;">
      <svg class="contact-icon" viewBox="0 0 40 40"><circle cx="20" cy="20" r="20" fill="var(--icon-gold)"/><path d="M9 18l11-8 11 8v12H9z" fill="#fff"/><rect x="17" y="22" width="6" height="8" fill="var(--icon-gold)"/></svg>
      <span>482 Tarrow Lane<br>Suite 207<br>Brenford, GA 30412</span>
    </div>

    <div class="contact-row" style="left:410px; top:478px;">
      <svg class="contact-icon" viewBox="0 0 40 40"><circle cx="20" cy="20" r="20" fill="var(--icon-gold)"/><circle cx="20" cy="20" r="11" fill="none" stroke="#fff" stroke-width="2.5"/><ellipse cx="20" cy="20" rx="5" ry="11" fill="none" stroke="#fff" stroke-width="2"/><line x1="9" y1="20" x2="31" y2="20" stroke="#fff" stroke-width="2"/></svg>
      <span>www.bvel7kga.com</span>
    </div>

    <div class="contact-row" style="left:378px; top:530px;">
      <svg class="contact-icon" viewBox="0 0 40 40"><circle cx="20" cy="20" r="20" fill="var(--icon-gold)"/><rect x="10" y="13" width="20" height="14" fill="#fff"/><path d="M10 13l10 8 10-8" fill="none" stroke="var(--icon-gold)" stroke-width="2"/></svg>
      <span>bvel7kga@quellmail.com</span>
    </div>
  </div>
</body>
</html>
```